Business card design needed

Special effects makeup artist.
I would love it to have my own photos on it. Because I do both SPFX (ghor) and beauty I would like the card on one side to be beauty and the other side SPFX.

If both sides can not be done that is fine, I still want it to represent BOTH sides of what I do paying more attention to the GHOR aspect please as its what I specialise in.

Its not letting me upload any photos but please go to

WWW.EXAMPLEBOOK.NET/VANTEFXART
As that's where my photos (well most of) are located. There is HEAPS of ghor on there.

Industry/Entity Type

Business

Contact Information for Business Card

Vante Quillmere ~ Makeup Artist Extraordinaire.
0491237785
MissQuillmere@mailnest.net
WWW.Examplebook.net/VanteFXArt

Logo Text

Vante Quillmere

Logo styles of interest
Wordmark Logo
Requirements
Must have
• My Photos
Blood Dripping
Nice to have
• My Photos
Zombie kind of design
Blood dripping writing
Lots of greens and reds
Should not have
• Flowers, swirls or REALLY girly things

```html
<!DOCTYPE html>
<html lang="en">
<head>
<meta charset="utf-8">
<title>Vante Quillmere – Business Card</title>
<link href="https://fonts.googleapis.com/css2?family=Quicksand:wght@400;500;700&display=swap" rel="stylesheet">
<style>
  :root {
    --bg-top: #3b3b3d;
    --bg-bottom: #1b1b1c;
    --rule: #ffffff;
    --name: #ffffff;
    --muted: #7c7c7e;
    --contact: #8e8e90;
    --icon: #ffffff;
  }
  html, body {
    margin: 0;
    padding: 0;
    width: 1200px;
    height: 652px;
    overflow: hidden;
    background: #ffffff;
  }
  .card {
    position: relative;
    width: 1200px;
    height: 652px;
    overflow: hidden;
    background:
      repeating-linear-gradient(-20deg, rgba(255,255,255,0.018) 0 2px, rgba(0,0,0,0.03) 2px 5px),
      linear-gradient(180deg, var(--bg-top) 0%, #2b2b2d 55%, var(--bg-bottom) 100%);
    font-family: "Quicksand", "Century Gothic", sans-serif;
  }
  .brand-name {
    position: absolute;
    left: 44px;
    top: 36px;
    margin: 0;
    font-size: 84px;
    font-weight: 700;
    color: var(--name);
    letter-spacing: 0.5px;
    line-height: 1.1;
  }
  .brand-role {
    position: absolute;
    left: 46px;
    top: 160px;
    margin: 0;
    font-size: 34px;
    font-weight: 500;
    color: var(--muted);
    letter-spacing: 0.5px;
  }
  .photo {
    position: absolute;
  }
  .photo--beauty-portrait {
    left: 1050px; top: 6px; width: 144px; height: 150px;
    background: linear-gradient(160deg, #5a3a2c 0%, #b98b72 50%, #e3c2ad 100%);
  }
  .photo--pinup-portrait {
    left: 887px; top: 161px; width: 157px; height: 154px;
    background: linear-gradient(150deg, #3a2520 0%, #c99682 55%, #b22b2b 100%);
  }
  .photo--fx-pale-face {
    left: 167px; top: 309px; width: 172px; height: 176px;
    background: radial-gradient(circle at 50% 50%, #f2f2f4 0%, #dcdde2 60%, #b9bccb 100%);
  }
  .photo--fx-dark-mask {
    left: 6px; top: 491px; width: 156px; height: 156px;
    background: linear-gradient(140deg, #5a1010 0%, #2a1a1a 45%, #d9d9d9 100%);
  }
  .grid-rules {
    position: absolute;
    left: 0; top: 0;
    width: 1200px; height: 652px;
  }
  .grid-rules line {
    stroke: var(--rule);
    stroke-width: 4;
  }
  .contact {
    position: absolute;
    left: 0; top: 0;
    margin: 0; padding: 0;
    list-style: none;
  }
  .contact__item {
    position: absolute;
    left: 492px;
    display: flex;
    align-items: center;
    white-space: nowrap;
  }
  .contact__icon {
    width: 70px;
    display: flex;
    justify-content: center;
    margin-right: 22px;
  }
  .contact__text {
    font-size: 33px;
    font-weight: 700;
    color: var(--contact);
  }
  .contact__item--phone { top: 382px; }
  .contact__item--email { top: 472px; }
  .contact__item--web { top: 566px; }
  .icon-square {
    width: 22px;
    height: 34px;
    background: var(--icon);
  }
</style>
</head>
<body>
  <main class="card">
    <h1 class="brand-name">Vante Quillmere</h1>
    <p class="brand-role">MAKEUP ARTIST EXTRAORDINAIRE</p>

    <div class="photo photo--beauty-portrait" role="img" aria-label="Beauty makeup portrait photo"></div>
    <div class="photo photo--pinup-portrait" role="img" aria-label="Pin-up style makeup portrait photo"></div>
    <div class="photo photo--fx-pale-face" role="img" aria-label="Special effects makeup photo with pale painted face"></div>
    <div class="photo photo--fx-dark-mask" role="img" aria-label="Special effects makeup photo with dark masked look"></div>

    <svg class="grid-rules" viewBox="0 0 1200 652" aria-hidden="true">
      <line x1="883" y1="6" x2="883" y2="360"/>
      <line x1="1046" y1="6" x2="1046" y2="381"/>
      <line x1="828" y1="157" x2="1194" y2="157"/>
      <line x1="728" y1="317" x2="1194" y2="317"/>
      <line x1="164" y1="244" x2="164" y2="647"/>
      <line x1="339" y1="269" x2="339" y2="647"/>
      <line x1="6" y1="308" x2="464" y2="308"/>
      <line x1="6" y1="487" x2="443" y2="487"/>
    </svg>

    <ul class="contact">
      <li class="contact__item contact__item--phone">
        <span class="contact__icon">
          <svg width="22" height="46" viewBox="0 0 22 46" aria-hidden="true">
            <rect x="16" y="0" width="3" height="9" fill="#fff"/>
            <rect x="2" y="8" width="18" height="36" rx="2" fill="none" stroke="#fff" stroke-width="2.5"/>
            <rect x="5" y="12" width="12" height="9" fill="#fff"/>
            <g fill="#fff">
              <rect x="5" y="25" width="3" height="2.5"/><rect x="9.5" y="25" width="3" height="2.5"/><rect x="14" y="25" width="3" height="2.5"/>
              <rect x="5" y="30" width="3" height="2.5"/><rect x="9.5" y="30" width="3" height="2.5"/><rect x="14" y="30" width="3" height="2.5"/>
              <rect x="5" y="35" width="3" height="2.5"/><rect x="9.5" y="35" width="3" height="2.5"/><rect x="14" y="35" width="3" height="2.5"/>
            </g>
          </svg>
        </span>
        <span class="contact__text">0491237785</span>
      </li>
      <li class="contact__item contact__item--email">
        <span class="contact__icon">
          <svg width="68" height="44" viewBox="0 0 68 44" aria-hidden="true">
            <rect x="2.5" y="2.5" width="63" height="39" fill="none" stroke="#fff" stroke-width="4"/>
            <polyline points="3,4 34,27 65,4" fill="none" stroke="#fff" stroke-width="4"/>
            <line x1="3" y1="40" x2="26" y2="21" stroke="#fff" stroke-width="4"/>
            <line x1="65" y1="40" x2="42" y2="21" stroke="#fff" stroke-width="4"/>
          </svg>
        </span>
        <span class="contact__text">MissQuillmere@mailnest.net</span>
      </li>
      <li class="contact__item contact__item--web">
        <span class="contact__icon"><span class="icon-square"></span></span>
        <span class="contact__text">www.Examplebook.net/VanteFXArt</span>
      </li>
    </ul>
  </main>
</body>
</html>
```